Stationery using new logo for pharmacy and gift shop

We need a letterhead, business card, gift voucher and possibly compliments slip design for our pharmacy and gift shop using our new logo.
The letterhead would need to be produced in both colour (purple and green) and grayscale and the business card would preferably be one-sided, but can be two-sided if this works better with the information it needs to have on it.

We would like a simple and elegant design, but not so simple that it looks like we've done it ourselves on Word. Use of our colours would be great but the letterhead would need to look good if printed on our black and white laser printer. If this is not possible then an additional version for grayscale would be needed.

We would need to receive high quality files that we can work with easily, such as pdf's for the letterhead that we can print instantly or order online as it appears on screen and business cards in jpeg and pdf so we can upload to printing sites.
We would like the vouchers in denominations of £5 and £10 in A5 size in a printable format such as PDF so that we don't have to resize.

Letterhead is for use in correspondence and invoicing to patients, surgeries, traders, customers etc.

Our preferred font is Orkney

Letterhead Info
Address
47 Fenwick Rd.
Harrowdale
Northvale
CA21 4QT

Tel: (01632) 960417
Fax: (01632) 960538
Website: www.brantleyspharmacy.example
Email: patientcare@brantleyspharmacy.example

Business Card Info.
As above but email address is: rkdbrantley@mailbox.example

Voucher Info.
Small print to state that any change will be paid as a credit note.
Space for a staff member to sign, date and stamp voucher

I have quite a few logo files so please ask if you need more uploaded. Or if you need more information to improve the design then please contact me.

Target Market(s)

Both retail customers and professional colleagues

Industry/Entity Type

Pharmacy

Font styles to use
Other font styles liked:
• orkney

Colors
ffffff
9bcb3c
6b449b

Requirements
Must have
• Must be clear and legible with a professional feel. Must use the logo well and all aspects of the designs should work well together.
• Final files MUST be easy to use for non-computer specialists. I need staff to be able to pull up a letterhead template easily if they are writing a letter or raising an invoice. The business card must be in a format ready to be sent to print.
Nice to have
• Letterhead available in a word processor program like word so that letters can be sent by email as well as print or print and scan.

```html
<!DOCTYPE html>
<html lang="en">
<head>
<meta charset="utf-8">
<title>Brantleys Pharmacy – Stationery Suite</title>
<link href="https://fonts.googleapis.com/css2?family=Questrial&family=Pinyon+Script&display=swap" rel="stylesheet">
<style>
:root{
  --purple:#6b449b;
  --purple-faint:rgba(107,68,155,.08);
  --green:#9bcb3c;
  --white:#ffffff;
  --paper:#f6f6f7;
  --ink:#6f6f78;
  --bg:#e4e4e6;
}
*{box-sizing:border-box;margin:0;padding:0}
html,body{width:1200px;height:721px;overflow:hidden;background:var(--bg)}
body{position:relative;font-family:"Questrial",sans-serif;color:var(--ink)}
.piece{position:absolute;overflow:hidden}

/* brand name */
.brand{display:flex;flex-direction:column;align-items:center;text-align:center;line-height:1}
.brand .mark{width:14px;height:14px;background:var(--purple);margin-bottom:5px}
.brand .name{color:var(--purple);font-size:9px;letter-spacing:.2px;white-space:nowrap}
.brand.on-purple .mark{background:var(--white)}
.brand.on-purple .name{color:var(--white)}

/* contact block */
.contact{font-size:4.3px;line-height:5.6px;color:var(--ink);border-left:.8px solid #c9c9cf;padding-left:6px}
.contact .row{display:flex;align-items:center;gap:3px;white-space:nowrap}
.contact .ico{width:4px;height:4px;background:var(--purple);border-radius:1px;flex:none}
.contact .ico.round{border-radius:50%}

.swoosh{position:absolute;left:0;bottom:0;width:100%}

/* business card front */
.card-front{left:126px;top:244px;width:184px;height:104px;background:var(--purple)}
.card-front .brand{position:absolute;left:0;right:0;top:34px}
.card-front .web{position:absolute;left:0;right:0;bottom:11px;text-align:center;color:var(--white);font-size:4.2px;letter-spacing:1.2px}

/* business card back */
.card-back{left:126px;top:367px;width:184px;height:104px;background:var(--paper)}
.card-back .brand{position:absolute;left:8px;top:38px;width:82px}
.card-back .brand .name{font-size:7.4px}
.card-back .contact{position:absolute;left:97px;top:20px;height:66px}
.card-back .person{color:var(--purple);font-size:6px;font-weight:bold;letter-spacing:.1px}
.card-back .role{color:var(--green);font-size:4.3px;margin-bottom:4px}

/* letterhead */
.letterhead{left:360px;top:64px;width:303px;height:426px;background:var(--paper)}
.letterhead .brand{position:absolute;left:22px;top:27px;width:100px}
.letterhead .contact{position:absolute;left:192px;top:30px}
.letterhead .watermark{position:absolute;left:78px;top:128px;width:148px;height:148px;border:10px solid var(--purple-faint);border-radius:4px}
.letterhead .letter{position:absolute;left:27px;top:120px;width:250px;font-size:4.1px;line-height:5.4px;color:#8a8a93}
.letterhead .salute{font-size:7.2px;color:#6a6a72;margin-bottom:12px}
.letterhead .letter p{margin-bottom:6px;text-align:justify}
.letterhead .signature{width:56px;height:18px;margin-top:6px;background:linear-gradient(90deg,rgba(107,68,155,.18),rgba(107,68,155,.05));border-radius:9px}
.letterhead .web{position:absolute;left:0;right:0;bottom:3px;text-align:center;color:var(--white);font-size:4.2px;letter-spacing:1.1px;z-index:2}

/* folder */
.folder{left:690px;top:38px;width:357px;height:452px;background:var(--purple)}
.folder .spine{position:absolute;top:0;bottom:0;width:1px;background:rgba(255,255,255,.22)}
.folder .watermark{position:absolute;left:60px;top:170px;width:240px;height:220px;background:rgba(255,255,255,.09);border-radius:4px}
.folder .brand{position:absolute;left:0;right:0;top:178px}
.folder .brand .mark{width:54px;height:54px;margin-bottom:14px}
.folder .brand .name{font-size:23.5px}

/* compliments slip */
.slip{left:62px;top:526px;width:350px;height:158px;background:var(--paper)}
.slip .brand{position:absolute;left:16px;top:16px;width:100px}
.slip .contact{position:absolute;left:250px;top:18px}
.slip .greeting{position:absolute;left:88px;top:88px;font-family:"Pinyon Script",cursive;font-size:26px;color:var(--purple);white-space:nowrap}

/* envelope front */
.env-front{left:432px;top:526px;width:350px;height:158px;background:var(--paper)}
.env-front .brand{position:absolute;left:10px;top:14px;width:100px}
.env-front .addr{font-size:4.2px;line-height:5.2px;color:var(--ink);margin-top:4px}
.env-front .watermark{position:absolute;left:230px;top:32px;width:100px;height:104px;border:8px solid var(--purple-faint);border-radius:3px}

/* envelope back */
.env-back{left:799px;top:525px;width:350px;height:158px;background:var(--paper)}
.env-back .flap{position:absolute;left:0;top:0;width:100%;height:50px}
.env-back .mark{position:absolute;left:165px;top:12px;width:20px;height:20px;border:2px solid var(--white)}
</style>
</head>
<body>

<section class="piece card-front" aria-label="Business card front">
  <div class="brand on-purple">
    <span class="mark"></span>
    <span class="name">BRANTLEYS PHARMACY</span>
  </div>
  <p class="web">www.brantleyspharmacy.example</p>
</section>

<section class="piece card-back" aria-label="Business card back">
  <div class="brand">
    <span class="mark"></span>
    <span class="name">BRANTLEYS PHARMACY</span>
  </div>
  <div class="contact">
    <p class="person">DANIEL REED</p>
    <p class="role">CEO/FOUNDER</p>
    <p>47 Fenwick Rd.</p>
    <p>Harrowdale</p>
    <p>Northvale</p>
    <p style="margin-bottom:3px">CA21 4QT</p>
    <p class="row"><span class="ico round"></span>(01632) 960417</p>
    <p class="row"><span class="ico"></span>(01632) 960538</p>
    <p class="row"><span class="ico"></span>rkdbrantley@mailbox.example</p>
    <p class="row"><span class="ico round"></span>www.brantleyspharmacy.example</p>
  </div>
</section>

<section class="piece letterhead" aria-label="Letterhead">
  <div class="brand">
    <span class="mark"></span>
    <span class="name">BRANTLEYS PHARMACY</span>
  </div>
  <div class="contact">
    <p>47 Fenwick Rd., Harrowdale</p>
    <p style="margin-bottom:3px">Northvale, CA21 4QT</p>
    <p class="row"><span class="ico round"></span>(01632) 960417</p>
    <p class="row"><span class="ico"></span>(01632) 960538</p>
    <p class="row"><span class="ico"></span>patientcare@brantleyspharmacy.example</p>
  </div>
  <div class="watermark"></div>
  <div class="letter">
    <p class="salute">Dear Mr. Reed,</p>
    <p>Thank you for your recent visit to our pharmacy. We are pleased to confirm that your repeat prescription is now ready for collection at the counter. Please bring a form of identification when you call in, and let our team know if you have any questions about your medicine.</p>
    <p>Our gift shop has also received a new range of seasonal items, including candles, cards and toiletries. Staff will be happy to help you choose something suitable for friends and family.</p>
    <p>We are open six days a week and offer free advice on minor ailments, health checks and travel vaccines. Appointments can be booked by phone or in person at the shop.</p>
    <p>If you would like to receive future updates by email, please reply with your preferred address and we will add you to our list.</p>
    <p style="margin-top:10px">Sincerely,</p>
    <div class="signature" role="img" aria-label="Handwritten signature"></div>
  </div>
  <svg class="swoosh" width="303" height="22" viewBox="0 0 303 22" aria-hidden="true">
    <path d="M0 11 Q151 -2 303 9 L303 22 L0 22 Z" fill="var(--purple)"/>
    <path d="M0 9 Q151 -4 303 7" fill="none" stroke="var(--green)" stroke-width="1"/>
  </svg>
  <p class="web">www.brantleyspharmacy.example</p>
</section>

<section class="piece folder" aria-label="Presentation folder">
  <span class="spine" style="left:6px"></span>
  <span class="spine" style="left:12px"></span>
  <span class="spine" style="left:18px"></span>
  <div class="watermark"></div>
  <div class="brand on-purple">
    <span class="mark"></span>
    <span class="name">BRANTLEYS PHARMACY</span>
  </div>
</section>

<section class="piece slip" aria-label="Compliments slip">
  <div class="brand">
    <span class="mark"></span>
    <span class="name">BRANTLEYS PHARMACY</span>
  </div>
  <div class="contact">
    <p>47 Fenwick Rd., Harrowdale</p>
    <p style="margin-bottom:3px">Northvale, CA21 4QT</p>
    <p class="row"><span class="ico round"></span>(01632) 960417</p>
    <p class="row"><span class="ico"></span>(01632) 960538</p>
    <p class="row"><span class="ico"></span>patientcare@brantleyspharmacy.example</p>
    <p class="row"><span class="ico round"></span>www.brantleyspharmacy.example</p>
  </div>
  <p class="greeting">With Compliments</p>
  <svg class="swoosh" width="350" height="24" viewBox="0 0 350 24" aria-hidden="true">
    <path d="M0 16 Q175 -4 350 16 L350 24 L0 24 Z" fill="var(--purple)"/>
    <path d="M0 14 Q175 -6 350 14" fill="none" stroke="var(--green)" stroke-width="1"/>
  </svg>
</section>

<section class="piece env-front" aria-label="Envelope front">
  <div class="brand">
    <span class="mark"></span>
    <span class="name">BRANTLEYS PHARMACY</span>
    <p class="addr">47 Fenwick Rd., Harrowdale<br>Northvale, CA21 4QT</p>
  </div>
  <div class="watermark"></div>
  <svg class="swoosh" width="350" height="24" viewBox="0 0 350 24" aria-hidden="true">
    <path d="M0 16 Q175 -4 350 16 L350 24 L0 24 Z" fill="var(--purple)"/>
    <path d="M0 14 Q175 -6 350 14" fill="none" stroke="var(--green)" stroke-width="1"/>
  </svg>
</section>

<section class="piece env-back" aria-label="Envelope back">
  <svg class="flap" viewBox="0 0 350 50" preserveAspectRatio="none" aria-hidden="true">
    <path d="M0 0 H350 V2 L343 30 Q340 48 322 48 H28 Q10 48 7 30 L0 2 Z" fill="var(--purple)"/>
  </svg>
  <span class="mark"></span>
</section>

</body>
</html>
```